Medical Device Packaging Project 1 of 5

We are a medical device startup company needing packaging for a total of 5 device brands. This is posting 1 of 5 and the device name is "Vexomira"

Vexomira is an intraocular lens for use in cataract surgery. The target market is Chinese ophthalmologists. The box should be sophisticated and upmarket.

The company name is Tambrel Vision, I have included the logo in the uploaded files section. You should include the logo on the box.

I have uploaded a sample lens boxes from other companies that demonstrate the information needed to be contained on the box in terms of address, warnings, symbols, etc.

I have also uploaded the blank dieline of the boxes

You are welcome and encouraged to also submit to projects 2, 3, 4, and 5 as well. The same rules and expectations apply.

Industry/Entity Type

It Company

Requirements
Should not have
• Should not have any images of an eye or any bionic/futuristic feel to the design
• Note that the quindaret box is for text reference only. You may use the lens image but the futuristic/bionic look is NOT what we are going for with this brand. It should be traditional upmarket medical device artwork.

```html
<!DOCTYPE html>
<html lang="en">
<head>
<meta charset="utf-8">
<title>Vexomira — Tambrel Vision</title>
<link rel="stylesheet" href="https://fonts.googleapis.com/css2?family=Open+Sans:wght@300;400;600;700&display=swap">
<style>
  :root {
    --page: #ffffff;
    --panel-light: #5fb0d4;
    --panel-mid: #3690bd;
    --panel-deep: #1f73a3;
    --side-deep: #1c6c9b;
    --side-light: #4aa0c8;
    --band: #0b5a86;
    --lens-light: #e6ecf1;
    --lens-mid: #b4c2cd;
    --white: #ffffff;
    --ghost: rgba(255, 255, 255, 0.16);
    --symbol: rgba(255, 255, 255, 0.85);
  }
  * { margin: 0; padding: 0; box-sizing: border-box; }
  html, body {
    width: 1200px;
    height: 871px;
    overflow: hidden;
    background: var(--page);
    font-family: "Open Sans", Arial, sans-serif;
  }
  .canvas { position: relative; width: 1200px; height: 871px; }

  /* Front face */
  .box-front {
    position: absolute;
    left: 110px;
    top: 146px;
    width: 780px;
    height: 580px;
    overflow: hidden;
    background:
      radial-gradient(circle at 15% 72%, rgba(255,255,255,0.22), transparent 26%),
      radial-gradient(circle at 82% 28%, rgba(255,255,255,0.30), transparent 30%),
      radial-gradient(circle at 90% 82%, rgba(255,255,255,0.16), transparent 24%),
      linear-gradient(135deg, var(--panel-deep) 0%, var(--panel-mid) 45%, var(--panel-light) 100%);
  }
  .ghost-brand {
    position: absolute;
    left: 18px;
    top: 118px;
    color: var(--ghost);
    text-align: center;
    line-height: 1;
  }
  .ghost-brand__name { display: block; font-size: 26px; font-weight: 300; letter-spacing: 3px; }
  .ghost-brand__sub { display: block; font-size: 11px; letter-spacing: 6px; margin-top: 6px; }
  .ghost-title {
    position: absolute;
    left: 526px;
    top: 28px;
    color: var(--ghost);
    font-size: 40px;
    font-weight: 600;
    letter-spacing: 3px;
  }
  .ghost-tagline {
    position: absolute;
    left: 528px;
    top: 86px;
    color: var(--ghost);
    font-size: 16px;
    line-height: 1.25;
  }

  /* Centre band */
  .centre-band {
    position: absolute;
    left: 166px;
    top: 0;
    width: 336px;
    height: 100%;
    background: var(--band);
  }
  .brand {
    position: absolute;
    top: 100px;
    left: 0;
    width: 100%;
    display: flex;
    align-items: center;
    justify-content: center;
    gap: 10px;
    color: var(--white);
    font-weight: 300;
    font-size: 27px;
    letter-spacing: 3px;
  }
  .brand-dot { width: 12px; height: 12px; border-radius: 50%; background: var(--white); }
  .lens-visual {
    position: absolute;
    left: 22px;
    top: 180px;
    width: 280px;
    height: 250px;
    border-radius: 50%;
    background: radial-gradient(ellipse at 45% 45%, var(--lens-light) 0%, var(--lens-mid) 75%, rgba(180,194,205,0) 100%);
    opacity: 0.92;
  }
  .product-name {
    position: absolute;
    top: 444px;
    left: 74px;
    color: var(--white);
    font-weight: 700;
    font-size: 29px;
    letter-spacing: 1.5px;
  }
  .rule {
    position: absolute;
    left: 74px;
    width: 226px;
    height: 1.5px;
    background: var(--white);
  }
  .rule--top { top: 490px; }
  .rule--bottom { top: 556px; }
  .product-use {
    position: absolute;
    top: 497px;
    left: 74px;
    width: 226px;
    text-align: center;
    color: var(--white);
    font-size: 16px;
    line-height: 1.2;
  }
  .product-use strong { font-weight: 700; }

  /* Side panel */
  .box-side {
    position: absolute;
    left: 890px;
    top: 146px;
    width: 190px;
    height: 580px;
    overflow: hidden;
    background:
      radial-gradient(circle at 40% 30%, rgba(255,255,255,0.22), transparent 40%),
      radial-gradient(circle at 60% 75%, rgba(255,255,255,0.16), transparent 35%),
      linear-gradient(160deg, var(--side-deep) 0%, var(--side-light) 100%);
  }
  .symbols {
    position: absolute;
    right: 24px;
    top: 70px;
    display: flex;
    flex-direction: column;
    align-items: center;
    gap: 22px;
  }
  .symbol { display: block; width: 18px; height: 18px; }
  .symbol--tall { width: 14px; height: 40px; }
  .side-brand {
    position: absolute;
    left: 60px;
    bottom: 30px;
    transform-origin: left bottom;
    transform: rotate(-90deg) translateY(100%);
    display: flex;
    align-items: center;
    gap: 10px;
    color: var(--white);
    font-weight: 300;
    font-size: 30px;
    letter-spacing: 3px;
    white-space: nowrap;
  }
</style>
</head>
<body>
  <main class="canvas">
    <section class="box-front">
      <p class="ghost-brand"><span class="ghost-brand__name">TAMBREL</span><span class="ghost-brand__sub">VISION</span></p>
      <span class="ghost-title">TAMBREL</span>
      <p class="ghost-tagline">Intraocular lens for use<br>in cataract surgery</p>

      <div class="centre-band">
        <div class="brand"><span class="brand-dot"></span>TAMBREL VISION</div>
        <div class="lens-visual" role="img" aria-label="Intraocular lens with two curved haptics"></div>
        <h1 class="product-name">VEXOMIRA</h1>
        <div class="rule rule--top"></div>
        <p class="product-use"><strong>Intraocular lens</strong> for use<br>in cataract surgery</p>
        <div class="rule rule--bottom"></div>
      </div>
    </section>

    <aside class="box-side">
      <div class="symbols" aria-label="Regulatory symbols">
        <svg class="symbol" viewBox="0 0 18 18"><circle cx="9" cy="9" r="7.5" fill="none" stroke="var(--symbol)" stroke-width="1.2"/><line x1="3.7" y1="14.3" x2="14.3" y2="3.7" stroke="var(--symbol)" stroke-width="1.2"/></svg>
        <svg class="symbol" viewBox="0 0 18 18"><circle cx="9" cy="9" r="7.5" fill="none" stroke="var(--symbol)" stroke-width="1.2"/><path d="M5 9h8M9 5v8" stroke="var(--symbol)" stroke-width="1.2"/></svg>
        <svg class="symbol" viewBox="0 0 18 18"><circle cx="9" cy="9" r="7.5" fill="none" stroke="var(--symbol)" stroke-width="1.2"/><line x1="3.7" y1="3.7" x2="14.3" y2="14.3" stroke="var(--symbol)" stroke-width="1.2"/></svg>
        <svg class="symbol" viewBox="0 0 18 18"><path d="M9 2 L16 15 H2 Z" fill="none" stroke="var(--symbol)" stroke-width="1.2"/><line x1="9" y1="7" x2="9" y2="11" stroke="var(--symbol)" stroke-width="1.2"/></svg>
        <svg class="symbol symbol--tall" viewBox="0 0 14 40"><rect x="1" y="1" width="12" height="24" fill="none" stroke="var(--symbol)" stroke-width="1"/><rect x="1" y="27" width="12" height="12" fill="none" stroke="var(--symbol)" stroke-width="1"/></svg>
      </div>
      <div class="side-brand"><span class="brand-dot"></span>TAMBREL VISION</div>
    </aside>
  </main>
</body>
</html>
```